Neighbourhood assistance

I need an app design for a social idea. Each person has some skils and could offer some assistance to some of his neighbours. With this app I will bring people together. For free or also for some money.That doesn't matter.

Please have a look into my pptx file which should give you an idea about the upcoming app.

Industry/Entity Type

Social

```html
<!DOCTYPE html>
<html lang="de">
<head>
<meta charset="utf-8">
<title>Interesten – Nachbarschaftshilfe</title>
<link rel="stylesheet" href="https://fonts.googleapis.com/css2?family=Nunito+Sans:wght@400;600;700&display=swap">
<style>
  :root {
    --stage-bg: #dfe2e6;
    --screen-bg: #eef0f3;
    --bar-blue: #2f86c8;
    --bar-blue-dark: #2874b0;
    --offer-orange: #ee7a22;
    --need-green: #2fc46c;
    --profile-blue: #3b93d6;
    --profile-blue-dark: #2a78b8;
    --white: #ffffff;
  }
  * { box-sizing: border-box; margin: 0; padding: 0; }
  html, body {
    width: 1200px;
    height: 800px;
    overflow: hidden;
    background: var(--stage-bg);
    font-family: "Nunito Sans", "Helvetica Neue", Arial, sans-serif;
  }
  .app-screen {
    position: absolute;
    left: 392px;
    top: 31px;
    width: 416px;
    height: 738px;
    background: var(--screen-bg);
    overflow: hidden;
    box-shadow: 0 10px 30px rgba(0,0,0,0.12);
  }
  .status-bar {
    height: 26px;
    background: var(--bar-blue);
    color: var(--white);
    font-size: 11px;
    font-weight: 600;
    display: flex;
    align-items: center;
    justify-content: space-between;
    padding: 0 8px;
  }
  .status-bar .carrier { display: flex; align-items: center; gap: 6px; }
  .status-bar .signal { display: flex; gap: 2px; }
  .status-bar .signal i {
    display: block; width: 5px; height: 5px; border-radius: 50%; background: var(--white);
  }
  .status-bar .battery { display: flex; align-items: center; gap: 4px; }
  .status-bar .battery-icon {
    width: 22px; height: 10px; border: 1px solid var(--white); border-radius: 2px; padding: 1px;
  }
  .status-bar .battery-icon span { display: block; width: 100%; height: 100%; background: var(--white); }
  .nav-bar {
    height: 57px;
    background: var(--bar-blue);
    color: var(--white);
    position: relative;
    display: flex;
    align-items: center;
    justify-content: center;
    font-size: 17px;
    font-weight: 700;
  }
  .nav-bar .back {
    position: absolute;
    left: 12px;
    top: 50%;
    transform: translateY(-50%);
  }
  .action-button {
    position: absolute;
    height: 44px;
    color: var(--white);
    font-size: 15px;
    font-weight: 600;
    display: flex;
    align-items: center;
    justify-content: center;
    border-radius: 2px;
  }
  .action-offer { left: 66px; top: 190px; width: 284px; background: var(--offer-orange); }
  .action-need  { left: 66px; top: 252px; width: 284px; background: var(--need-green); }
  .profile-button {
    position: absolute;
    left: 0;
    top: 400px;
    width: 296px;
    height: 50px;
    display: flex;
    background: var(--profile-blue);
    color: var(--white);
    font-size: 15px;
    font-weight: 600;
  }
  .profile-button .icon-cell {
    width: 50px;
    background: var(--profile-blue-dark);
    display: flex;
    align-items: center;
    justify-content: center;
  }
  .profile-button .label {
    flex: 1;
    display: flex;
    align-items: center;
    justify-content: center;
  }
</style>
</head>
<body>
  <main class="app-screen">
    <div class="status-bar">
      <div class="carrier">
        <span class="signal"><i></i><i></i><i></i><i></i><i></i></span>
        <span>Nordnetz</span>
      </div>
      <span class="clock">4:21 PM</span>
      <div class="battery">
        <span>100%</span>
        <span class="battery-icon"><span></span></span>
      </div>
    </div>
    <header class="nav-bar">
      <svg class="back" width="12" height="20" viewBox="0 0 12 20" aria-label="Zurück">
        <polyline points="10,2 2,10 10,18" fill="none" stroke="#ffffff" stroke-width="2.2" stroke-linecap="round" stroke-linejoin="round"/>
      </svg>
      <h1 style="font-size:inherit;font-weight:inherit;">Interesten</h1>
    </header>

    <div class="action-button action-offer">Du bietest an...</div>
    <div class="action-button action-need">Du brauchst...</div>

    <div class="profile-button">
      <span class="icon-cell">
        <svg width="18" height="18" viewBox="0 0 18 18" aria-hidden="true">
          <circle cx="9" cy="5.5" r="4" fill="#ffffff"/>
          <path d="M1 17c0-4.4 3.6-7 8-7s8 2.6 8 7z" fill="#ffffff"/>
        </svg>
      </span>
      <span class="label">Profil anpassen</span>
    </div>
  </main>
</body>
</html>
```